Stationary for Automotive Paintless Dent Repair Company
Panel Soothe LLC
Stationary for Automotive Paintless Dent Repair Company - Automotive
Creative Brief
Modern
Mark Fenley
Owner
478 Birch Ln Allentown, PA 18117
info@PanelSootheLLC.com
www.SmoothMyPanels.com
I would like to see both light and dark examples. I'm open to any kind of design. I prefer a sleek, modern theme to go along with the logo. Linkora, Ravo, and Clipverse logos can also be added.
Logo and/or web address. Open to all suggestions and ideas. Have fun with it!

```html
<!DOCTYPE html>
<html lang="en">
<head>
<meta charset="utf-8">
<title>Panel Soothe LLC – Business Cards</title>
<link rel="stylesheet" href="https://fonts.googleapis.com/css2?family=Montserrat:wght@400;500;600;800&display=swap">
<style>
  :root {
    --bg: #e9ebee;
    --card-white: #ffffff;
    --blue-deep: #0b4fae;
    --blue-mid: #1f6fdc;
    --blue-light: #3b8ff0;
    --swoosh-grey: #8d9299;
    --black-card: #16181b;
    --black-card-edge: #2a2d31;
    --text-white: #ffffff;
    --logo-blue: #1d74d8;
    --tag-grey: #5d636b;
    --tag-light: #c4c8ce;
  }
  * { box-sizing: border-box; margin: 0; padding: 0; }
  html, body { width: 1200px; height: 901px; overflow: hidden; }
  body {
    background: var(--bg);
    font-family: "Montserrat", Arial, sans-serif;
    display: flex;
    align-items: center;
    justify-content: center;
    gap: 60px;
  }
  .card {
    position: relative;
    width: 520px;
    height: 300px;
    border-radius: 18px;
    overflow: hidden;
    box-shadow: 0 10px 28px rgba(0,0,0,0.18);
  }
  .card-front { background: var(--card-white); }
  .card-front .card-bg { position: absolute; inset: 0; }

  .brand {
    position: absolute;
    display: flex;
    flex-direction: column;
    align-items: flex-start;
  }
  .brand-row { display: flex; align-items: center; gap: 7px; }
  .brand-dot {
    width: 10px; height: 10px; border-radius: 50%;
    background: var(--logo-blue);
    flex: none;
  }
  .brand-name {
    font-weight: 800;
    font-size: 20px;
    letter-spacing: 0.4px;
    color: var(--logo-blue);
    text-transform: uppercase;
    line-height: 1;
    white-space: nowrap;
  }
  .brand-tagline {
    margin-top: 5px;
    margin-left: 17px;
    font-size: 7.5px;
    font-weight: 500;
    letter-spacing: 2px;
    color: var(--tag-grey);
    text-transform: uppercase;
    white-space: nowrap;
  }
  .card-front .brand { left: 24px; top: 122px; }

  .contact {
    position: absolute;
    right: 24px;
    top: 0;
    bottom: 0;
    width: 210px;
    color: var(--text-white);
    text-align: right;
  }
  .person { position: absolute; right: 0; top: 56px; }
  .person-name {
    font-size: 15px; font-weight: 500; letter-spacing: 0.8px;
    text-transform: uppercase; white-space: nowrap;
  }
  .person-title { font-size: 11px; margin-top: 3px; }

  .address {
    position: absolute; right: 0; top: 130px;
    font-size: 10.5px; line-height: 15px; white-space: nowrap;
  }
  .lines {
    position: absolute; right: 0; top: 186px;
    list-style: none;
  }
  .lines li {
    display: flex; justify-content: flex-end; align-items: center;
    gap: 7px; font-size: 10.5px; height: 19px; white-space: nowrap;
  }
  .lines svg { width: 11px; height: 11px; flex: none; }

  .card-back {
    background: linear-gradient(160deg, var(--black-card-edge), var(--black-card) 55%);
    display: flex; align-items: center; justify-content: center;
  }
  .card-back .brand { position: static; }
  .card-back .brand-name { font-size: 24px; }
  .card-back .brand-dot { width: 12px; height: 12px; }
  .card-back .brand-tagline { color: var(--tag-light); font-size: 8.5px; margin-left: 19px; }
</style>
</head>
<body>

<section class="card card-front" aria-label="Business card front">
  <svg class="card-bg" viewBox="0 0 520 300" preserveAspectRatio="none" aria-hidden="true">
    <defs>
      <linearGradient id="blueField" x1="0" y1="0" x2="1" y2="1">
        <stop offset="0" stop-color="#3b8ff0"/>
        <stop offset="0.55" stop-color="#1f6fdc"/>
        <stop offset="1" stop-color="#0b4fae"/>
      </linearGradient>
    </defs>
    <path d="M335,0 C285,70 285,210 235,300 L520,300 L520,0 Z" fill="url(#blueField)"/>
    <path d="M323,0 C273,70 273,210 223,300" fill="none" stroke="#8d9299" stroke-width="5" opacity="0.8"/>
  </svg>

  <div class="brand">
    <div class="brand-row">
      <span class="brand-dot"></span>
      <span class="brand-name">Panel Soothe</span>
    </div>
    <span class="brand-tagline">Paintless Dent Removal</span>
  </div>

  <div class="contact">
    <div class="person">
      <p class="person-name">Mark Fenley</p>
      <p class="person-title">Managing Director</p>
    </div>
    <p class="address">478 Birch Ln<br>Allentown, PA 18117</p>
    <ul class="lines">
      <li>610 555 0142
        <svg viewBox="0 0 12 12"><path d="M2.5 1 L4.5 1 L5.3 3.3 L4 4.3 C4.7 5.8 6.2 7.3 7.7 8 L8.7 6.7 L11 7.5 L11 9.5 C11 10.3 10.3 11 9.5 11 C5 10.7 1.3 7 1 2.5 C1 1.7 1.7 1 2.5 1 Z" fill="#fff"/></svg>
      </li>
      <li>610 555 0143
        <svg viewBox="0 0 12 12"><rect x="3" y="0.5" width="6" height="11" rx="1.2" fill="none" stroke="#fff" stroke-width="1.2"/><circle cx="6" cy="9.5" r="0.7" fill="#fff"/></svg>
      </li>
      <li>610 555 0144
        <svg viewBox="0 0 12 12"><rect x="1" y="2" width="10" height="8" rx="1" fill="#fff"/><rect x="3" y="4" width="6" height="2" fill="#1f6fdc"/></svg>
      </li>
      <li>info@PanelSootheLLC.com
        <svg viewBox="0 0 12 12"><rect x="0.8" y="2.2" width="10.4" height="7.6" fill="#fff"/><path d="M0.8 2.2 L6 6.5 L11.2 2.2" fill="none" stroke="#1f6fdc" stroke-width="1"/></svg>
      </li>
      <li>www.SmoothMyPanels.com
        <svg viewBox="0 0 12 12"><circle cx="6" cy="6" r="5" fill="none" stroke="#fff" stroke-width="1.1"/><ellipse cx="6" cy="6" rx="2.2" ry="5" fill="none" stroke="#fff" stroke-width="0.9"/><line x1="1" y1="6" x2="11" y2="6" stroke="#fff" stroke-width="0.9"/></svg>
      </li>
    </ul>
  </div>
</section>

<section class="card card-back" aria-label="Business card back">
  <div class="brand">
    <div class="brand-row">
      <span class="brand-dot"></span>
      <span class="brand-name">Panel Soothe</span>
    </div>
    <span class="brand-tagline">Paintless Dent Removal</span>
  </div>
</section>

</body>
</html>
```